Heartnight Soiree- The Tailored Gala

This is an elegant Dinner concert event for Valentines day February 14 2020 in Vancouver WA. Live R&B band.

Join us for an Evening of live R&B music Featuring some of Oregon and Washington's talented music artists

Tickets prices: $30 concert only pp
$60 dinner and concert pp
$90 VIP Dinner & one drink/Concert/Premium Seating/Special Gift pp
Doors open @ 6:45 Event is 7:30 to 10:30
Location: Larkspur
417 Fenwick Ave.B Vancouver, WA 98664

www.teamhollowfen.com for more info.

Target Market(s)

Adults /Couples

Industry/Entity Type

Entertainment Industry

Font styles to use
Sans Serif
Decorative

Colors

Designer to choose colors to be used in the design.

Requirements
Must have
• Add the logos for Sponsors of the Event. Brindles is the main sponsor of the event.
• Main colors should be Red and right for valentine. Needs to be sized for a 5x7 Flyer
• Include the pictures of the Music Artists

```html
<!DOCTYPE html>
<html lang="en">
<head>
<meta charset="utf-8">
<title>Valentines Day Dinner Concert</title>
<link rel="stylesheet" href="https://fonts.googleapis.com/css2?family=Cinzel:wght@400;600&family=Parisienne&family=Montserrat:wght@600;700&display=swap">
<style>
  :root {
    --red-deep: #7a0d0c;
    --red: #d8261a;
    --red-bright: #f0452c;
    --ink-dark: #3a1010;
    --white: #ffffff;
    --gold-light: #f4dc8a;
    --gold: #c99a3a;
    --band: rgba(40, 14, 14, 0.55);
  }
  * { margin: 0; padding: 0; box-sizing: border-box; }
  html, body { width: 857px; height: 1200px; overflow: hidden; background: #fff; }
  .flyer {
    position: relative; width: 857px; height: 1200px; overflow: hidden;
    font-family: "Cinzel", serif; color: var(--white);
  }
  .backdrop {
    position: absolute; inset: 0;
    background:
      radial-gradient(ellipse 60% 35% at 60% 25%, rgba(255,120,80,.55), transparent 70%),
      radial-gradient(ellipse 50% 40% at 10% 5%, rgba(40,40,60,.8), transparent 70%),
      radial-gradient(ellipse 40% 25% at 20% 90%, rgba(150,10,20,.7), transparent 70%),
      linear-gradient(180deg, #a8251d 0%, #d83a24 35%, #e0341f 60%, #d42a1f 85%, #e86a4e 100%);
  }
  .title { position: absolute; left: 0; width: 100%; text-align: center; }
  .title-script {
    top: 150px; left: 40px; font-family: "Parisienne", cursive;
    font-size: 104px; line-height: 1; font-weight: 400;
  }
  .title-main {
    font-size: 98px; line-height: 1; letter-spacing: 1px; left: 0;
  }
  .title-dinner { top: 244px; left: -10px; }
  .title-concert { top: 328px; left: 50px; font-size: 104px; }
  .intro {
    position: absolute; top: 462px; left: 220px; width: 446px; text-align: center;
    font-size: 18px; letter-spacing: 4.5px; line-height: 26px; font-weight: 400;
  }
  .doors {
    position: absolute; top: 583px; left: 0; width: 100%; height: 38px;
    background: linear-gradient(90deg, transparent, var(--band) 12%, var(--band) 88%, transparent);
    text-align: center; font-family: "Cinzel", serif; font-size: 21px; line-height: 38px;
  }
  .artists { position: absolute; top: 623px; left: 9px; display: flex; gap: 6px; }
  .artist { width: 206px; height: 224px; }
  .artist-1 { background: linear-gradient(160deg, #3a0e0c, #6a1a14 60%, #2a0808); }
  .artist-2 { background: linear-gradient(160deg, #c46a4a, #7a2a1c 60%, #e8c0a8); }
  .artist-3 { background: linear-gradient(160deg, #4a1510, #9a3a28 60%, #5a1a14); }
  .artist-4 { background: linear-gradient(160deg, #5a1a14, #8a2418 60%, #3a0c0a); }
  .venue {
    position: absolute; top: 878px; left: 210px; display: flex; align-items: center; gap: 12px;
  }
  .venue-lines { font-size: 21px; letter-spacing: 3.5px; line-height: 26px; }
  .prices {
    position: absolute; top: 940px; left: 86px; width: 720px; display: flex; align-items: center;
  }
  .price { display: flex; align-items: center; margin-right: 14px; }
  .price-amount {
    font-family: "Cinzel", serif; font-weight: 600; font-size: 62px; letter-spacing: -3px;
    background: linear-gradient(180deg, var(--gold-light), var(--gold));
    -webkit-background-clip: text; background-clip: text; color: transparent;
  }
  .price-note {
    font-size: 14px; line-height: 13px; margin-left: 4px; font-weight: 600;
  }
  .sponsors {
    position: absolute; top: 1039px; left: 56px; width: 746px; height: 92px;
    border: 2px solid var(--white); display: flex; align-items: center; justify-content: space-around;
  }
  .sponsors-label {
    position: absolute; top: -11px; left: 50%; transform: translateX(-50%);
    background: #d52c1f; padding: 0 18px; color: var(--ink-dark);
    font-size: 15px; letter-spacing: 4px; font-weight: 600;
  }
  .sponsor {
    display: flex; align-items: center; gap: 8px;
    font-family: "Montserrat", sans-serif; font-weight: 700; font-size: 26px;
  }
  .sponsor-mark { width: 22px; height: 22px; background: var(--white); border-radius: 50%; }
  .sponsor-small { font-size: 16px; }
  .website {
    position: absolute; top: 1152px; left: 0; width: 100%; text-align: center;
    font-size: 19px; letter-spacing: 4.5px;
  }
</style>
</head>
<body>
<main class="flyer">
  <div class="backdrop" role="img" aria-label="Warm red candlelit photo of two wine glasses touching beside a candle and roses"></div>

  <h1>
    <span class="title title-script">Valentines Day</span>
    <span class="title title-main title-dinner">DINNER</span>
    <span class="title title-main title-concert">CONCERT</span>
  </h1>

  <p class="intro">Join us for an Evening of live R&amp;B music Featuring some of Oregon and Washington's talented music artists</p>

  <p class="doors">DOORS OPEN @ 6:45 EVENT IS 7:30 TO 10:30</p>

  <section class="artists">
    <div class="artist artist-1" role="img" aria-label="Portrait of featured singer"></div>
    <div class="artist artist-2" role="img" aria-label="Portrait of featured singer"></div>
    <div class="artist artist-3" role="img" aria-label="Portrait of featured singer"></div>
    <div class="artist artist-4" role="img" aria-label="Portrait of featured singer"></div>
  </section>

  <address class="venue">
    <svg width="30" height="42" viewBox="0 0 30 42" aria-hidden="true">
      <path d="M15 0C6.7 0 0 6.7 0 15c0 10 15 27 15 27s15-17 15-27C30 6.7 23.3 0 15 0z" fill="#fff"/>
      <circle cx="15" cy="15" r="5.5" fill="#d8261a"/>
    </svg>
    <div class="venue-lines">LARKSPUR, 417 FENWICK AVE.<br>B VANCOUVER, WA 98664</div>
  </address>

  <section class="prices">
    <div class="price"><span class="price-amount">$30</span><span class="price-note">CONCERT<br>ONLY PP</span></div>
    <div class="price"><span class="price-amount">$60</span><span class="price-note">DINNER AND<br>CONCERT PP</span></div>
    <div class="price"><span class="price-amount">$90</span><span class="price-note">VIP DINNER &amp; ONE<br>DRINK CONCERT<br>PREMIUM SEATING<br>SPECIAL GIFT PP</span></div>
  </section>

  <section class="sponsors">
    <span class="sponsors-label">SPONSORS</span>
    <div class="sponsor"><span class="sponsor-mark"></span>BRINDLES</div>
    <div class="sponsor"><span class="sponsor-mark"></span>ENCORE GUILD</div>
    <div class="sponsor sponsor-small">The Marlow Bloom</div>
  </section>

  <p class="website">WWW.TEAMHOLLOWFEN.COM</p>
</main>
</body>
</html>
```